Need Primer (paint) Label Design

THE ATTACHED LABEL/S ARE SOLEY FOR REFERENCE. DO NOT MAKE ME AN INTERIOR PAINT OR CHALK PAINT LABEL. I ONLY NEED A "PRIMER" LABEL. THE ATTACHED INTERIOR PAINT LABEL IS ONLY TO SHOW YOU THE THEME/DESIGN OF OUR OTHER LABELS. THE BLUE LABEL ONLY HAS A DESIGN ASPECT I LIKE (PRIMER ON SIDE). The last four labels are our competitors.
```````````````````````````````````````````````````````````````````````````````````````````````````
We need this label to look professional, sharp, eye catching and modern.
OUR PRIMARY COLORS ARE BLACK AND WHITE. IF YOU INCOPORATE ANOTHER COLOR, SILVER OR GOLD MIGHT BE IDEAL BUT PLEASE DON'T DRIFT TOO FAR.
The attached documents:
1st - Our Logo
2nd - Our chalk paint label (reference). We do not need a chalk paint label.
3rd. A random design example. I like the PRIME on the side running vertically. I think it's a cool design concept.
````````````````````````````````````````````````````````````````````````````````````````````````````
We are going to be using a normal paint can with a metal bail/handle so please use that with you design work
``````````````````````````````````````````````````````````````````````````````````````````````````
Order, in my head:
2743
Coatings
^^ I want this to stand out as well but I don't want it to be the first thing your eye is drawn to. Probably 2nd
Interior/Exterior
Multi - Surface Primer
^^ Want this to stick out and draw your eye so the customer knows what it is immediately
Exceptional Adhesion, Performance, Durability,
Use on Wood, Drywall, Plaster, Stucco, Masonry, Brick, Paneling, Painted Metal, & Properly Prepared Glossy Surfaces & More
35* Lowe Temperature Application (can be on side or small)
100% Acrylic
Low Odor - Low VOC - Soap & Water Clean Up
1 US Gallon - 3.785 L
Feel free to get creative with it!

```html
<!DOCTYPE html>
<html lang="en">
<head>
<meta charset="utf-8">
<title>2743 Coatings – Multi-Surface Primer Label</title>
<link href="https://fonts.googleapis.com/css2?family=Jost:wght@400;500;700&display=swap" rel="stylesheet">
<style>
  :root {
    --backdrop: #dcdcdd;
    --label-black: #111112;
    --label-white: #f2f2f2;
    --silver-light: #e4e4e6;
    --silver-mid: #a9a9ad;
    --silver-dark: #6f6f74;
    --ink: #1c1c1e;
    --icon-line: #d6d6d8;
  }
  * { margin: 0; padding: 0; box-sizing: border-box; }
  html, body { width: 1200px; height: 873px; overflow: hidden; }
  body {
    background: var(--backdrop);
    font-family: "Jost", sans-serif;
    position: relative;
  }
  .label {
    position: absolute;
    left: 338px; top: 143px;
    width: 541px; height: 635px;
    background: var(--label-white);
    overflow: hidden;
  }
  .label__top {
    position: absolute; left: 0; top: 0;
    width: 100%; height: 404px;
    background: radial-gradient(ellipse at 50% 40%, #1d1d1f 0%, var(--label-black) 70%);
  }
  .label__band {
    position: absolute; left: 0; top: 404px;
    width: 100%; height: 14px;
    background: linear-gradient(90deg, var(--silver-dark), var(--silver-light) 35%, #ffffff 55%, var(--silver-mid) 80%, var(--silver-dark));
  }
  .brand-name {
    position: absolute; left: 0; top: 92px; width: 100%;
    text-align: center; color: #ececec;
    font-size: 40px; font-weight: 400; line-height: 1;
  }
  .product-title {
    position: absolute; left: 0; top: 200px; width: 100%;
    text-align: center; font-weight: 700; font-size: 31px; line-height: 38px;
    color: var(--silver-mid); letter-spacing: 0.5px;
  }
  .product-title span { color: var(--silver-light); }
  .features {
    position: absolute; left: 70px; top: 312px; width: 405px;
    display: flex; justify-content: space-between;
  }
  .feature {
    width: 120px; text-align: center; color: var(--icon-line);
    font-size: 10px; line-height: 12px; font-weight: 500;
  }
  .feature svg { display: block; margin: 0 auto 8px; width: 38px; height: 38px; }
  .surfaces {
    position: absolute; left: 0; top: 456px; width: 100%;
    text-align: center; color: var(--ink); font-size: 10.5px; line-height: 15px;
  }
  .specs {
    position: absolute; left: 0; top: 512px; width: 100%;
    text-align: center; color: var(--ink); font-size: 15px; line-height: 21px; font-weight: 500;
  }
  .volume {
    position: absolute; left: 50%; top: 586px; transform: translateX(-50%);
    background: var(--label-black); color: #fff; border-radius: 9px;
    font-size: 10.5px; font-weight: 500; letter-spacing: 1.2px; padding: 2px 10px;
    white-space: nowrap;
  }
  .temp-note {
    position: absolute; left: 0; top: 618px; width: 100%;
    text-align: center; color: var(--ink); font-size: 7px;
  }
</style>
</head>
<body>
  <div class="label">
    <div class="label__top"></div>
    <div class="label__band"></div>

    <div class="brand-name">2743 Coatings</div>

    <div class="product-title">
      <div><span>INTERIOR|EXTERIOR</span></div>
      <div>MULTI - <span>SURFACE</span> PRIMER</div>
    </div>

    <div class="features">
      <div class="feature">
        <svg viewBox="0 0 40 40" fill="none" stroke="currentColor" stroke-width="1.6" stroke-linejoin="round">
          <path d="M20 4 L34 12 L20 20 L6 12 Z"/>
          <path d="M6 20 L20 28 L34 20"/>
          <path d="M14 23 V17 M20 26 V19 M26 23 V17"/>
        </svg>
        EXCEPTIONAL<br>ADHESION
      </div>
      <div class="feature">
        <svg viewBox="0 0 40 40" fill="none" stroke="currentColor" stroke-width="1.6" stroke-linejoin="round">
          <path d="M9 12 Q20 -2 31 12"/>
          <ellipse cx="20" cy="14" rx="12" ry="3"/>
          <path d="M8 14 V34 Q20 38 32 34 V14"/>
          <path d="M12 17 V26 M17 17 V29 M22 17 V24 M27 17 V28"/>
        </svg>
        PERFORMANCE
      </div>
      <div class="feature">
        <svg viewBox="0 0 40 40" fill="none" stroke="currentColor" stroke-width="1.6" stroke-linejoin="round">
          <circle cx="20" cy="20" r="17"/>
          <path d="M20 8 L29 11 V19 Q29 27 20 31 Q11 27 11 19 V11 Z"/>
          <path d="M16 19 L19 22 L25 16"/>
        </svg>
        DURABILITY
      </div>
    </div>

    <p class="surfaces">Use on Wood, Drywall, Plaster, Stucco, Masonry, Brick, Paneling,<br>Painted Metal, &amp; Properly Prepared Glossy Surfaces &amp; More</p>

    <p class="specs">100% ACRYLIC • LOW ODOR • LOW VOC<br>SOAP &amp; WATER CLEAN UP</p>

    <div class="volume">ONE GALLON / 3.75 L</div>

    <p class="temp-note">35* Lowe Temperature Application</p>
  </div>
</body>
</html>
```